RJ Heating & Cooling / 2018 Varden Kestrel Medium Roof / 148"wb

Customer is looking for a new design on his new 2018 varden kestrel medium roof 148"wb van. This will be a Full Wrap.

Attached is: >Customers logo
> Template for the van he has (You don't have to use this exact one for the proof)

Please include: > Slogan- Quality work at reasonable prices
>(555) 014-2293
>Services- Repairs, installation, maintenance, water heaters, indoor air quality
>Residential & Commercial

```html
<!DOCTYPE html>
<html lang="en">
<head>
<meta charset="utf-8">
<title>RJ Heating &amp; Cooling – Van Wrap</title>
<link rel="stylesheet" href="https://fonts.googleapis.com/css2?family=Luckiest+Guy&family=Fredoka:wght@600&display=swap">
<style>
  :root {
    --backdrop: #e8e8e8;
    --wrap-orange: #f58a1f;
    --wrap-blue: #3a7fd9;
    --wrap-blue-light: #5b9cf0;
    --wrap-white: #ffffff;
    --trim-dark: #2f2f31;
    --glass: #3c3d40;
    --tyre: #262628;
    --rim: #bfc3c7;
    --phone-blue: #2fb0f0;
    --text-white: #ffffff;
    --text-edge: #1d3f73;
  }
  * { margin: 0; padding: 0; box-sizing: border-box; }
  html, body {
    width: 1200px; height: 1001px; overflow: hidden;
    background: var(--backdrop);
  }
  .canvas { position: relative; width: 1200px; height: 1001px; }
  .van-side { position: absolute; inset: 0; }
  .wrap-copy { position: absolute; inset: 0; pointer-events: none; }
  .brand-name {
    position: absolute; left: 130px; top: 292px; width: 330px;
    font-family: "Luckiest Guy", "Fredoka", sans-serif;
    font-size: 46px; line-height: 1.05; color: var(--text-white);
    white-space: nowrap;
  }
  .call-label {
    position: absolute; left: 130px; top: 410px;
    font-family: "Luckiest Guy", "Fredoka", sans-serif;
    font-size: 34px; line-height: 1; color: var(--text-white);
  }
  .phone {
    position: absolute; left: 130px; top: 502px;
    display: flex; align-items: center; gap: 8px;
    font-family: "Luckiest Guy", "Fredoka", sans-serif;
    font-size: 38px; line-height: 1; color: var(--phone-blue);
    white-space: nowrap;
  }
  .phone svg { width: 28px; height: 28px; }
  .services {
    position: absolute; left: 612px; top: 516px; width: 300px;
    font-family: "Fredoka", sans-serif; font-weight: 600;
    font-size: 17px; line-height: 1.35; color: var(--text-white);
  }
  .slogan {
    position: absolute; left: 620px; top: 594px;
    font-family: "Fredoka", sans-serif; font-weight: 600;
    font-size: 24px; line-height: 1; color: var(--text-white);
    white-space: nowrap;
    text-shadow: 0 0 3px var(--text-edge), 0 0 3px var(--text-edge);
  }
  .sectors {
    position: absolute; left: 340px; top: 672px; width: 490px;
    text-align: center;
    font-family: "Fredoka", sans-serif; font-weight: 600;
    font-size: 20px; line-height: 1; color: var(--text-white);
  }
</style>
</head>
<body>
<div class="canvas">
  <svg class="van-side" viewBox="0 0 1200 1001" xmlns="http://www.w3.org/2000/svg">
    <defs>
      <clipPath id="body-outline">
        <path d="M92,300 Q92,262 140,258 L760,248 Q838,248 900,300 L1010,428 Q1098,456 1110,520 L1110,700 Q1110,740 1070,740 L120,740 Q92,740 92,705 Z"/>
      </clipPath>
    </defs>

    <g class="wrap-panels" clip-path="url(#body-outline)">
      <rect class="panel-white" x="80" y="240" width="1050" height="520" fill="var(--wrap-white)"/>
      <polygon class="panel-blue" points="500,240 840,240 1000,760 660,760" fill="var(--wrap-blue)"/>
      <polygon class="panel-blue-tint" points="640,240 840,240 910,470 710,470" fill="var(--wrap-blue-light)" opacity="0.45"/>
      <polygon class="panel-orange" points="80,240 460,240 620,760 80,760" fill="var(--wrap-orange)"/>
      <rect class="lower-trim" x="80" y="660" width="1050" height="50" fill="var(--trim-dark)"/>
      <rect class="front-bumper" x="930" y="620" width="200" height="140" fill="var(--trim-dark)"/>
    </g>

    <path class="side-window" d="M640,300 L780,300 L840,420 L840,470 L650,470 Q636,470 636,456 Z" fill="var(--glass)"/>
    <path class="windscreen" d="M800,268 Q850,270 895,305 L990,420 L870,420 Z" fill="var(--glass)"/>
    <rect class="rub-strip" x="120" y="472" width="230" height="12" rx="4" fill="var(--trim-dark)"/>
    <rect class="door-handle" x="660" y="484" width="44" height="10" rx="5" fill="var(--trim-dark)"/>
    <rect class="door-handle" x="718" y="484" width="44" height="10" rx="5" fill="var(--trim-dark)"/>
    <path class="headlamp" d="M1040,470 L1100,490 L1104,540 L1050,530 Z" fill="#d7dadd"/>

    <g class="wheel rear-wheel">
      <circle cx="255" cy="745" r="72" fill="var(--tyre)"/>
      <circle cx="255" cy="745" r="40" fill="var(--rim)"/>
      <circle cx="255" cy="745" r="12" fill="#8d9196"/>
    </g>
    <g class="wheel front-wheel">
      <circle cx="905" cy="745" r="72" fill="var(--tyre)"/>
      <circle cx="905" cy="745" r="40" fill="var(--rim)"/>
      <circle cx="905" cy="745" r="12" fill="#8d9196"/>
    </g>
  </svg>

  <div class="wrap-copy">
    <div class="brand-name">RJ Heating<br>&amp; Cooling</div>
    <div class="call-label">Call Us:</div>
    <div class="phone">
      <svg viewBox="0 0 24 24" aria-hidden="true"><path fill="currentColor" d="M6.6 10.8a15.1 15.1 0 0 0 6.6 6.6l2.2-2.2a1 1 0 0 1 1-.25 11.4 11.4 0 0 0 3.6.57 1 1 0 0 1 1 1V20a1 1 0 0 1-1 1A17 17 0 0 1 3 4a1 1 0 0 1 1-1h3.5a1 1 0 0 1 1 1c0 1.25.2 2.45.57 3.6a1 1 0 0 1-.25 1z"/></svg>
      <span>(555) 014-2293</span>
    </div>
    <div class="services">Repairs · Installation · Maintenance<br>Water Heaters · Indoor Air Quality</div>
    <div class="slogan">Quality work at reasonable prices</div>
    <div class="sectors">Residential &amp; Commercial</div>
  </div>
</div>
</body>
</html>
```